Emergency Vehicle Installer and Security Firm Needs a Business Card

Our company "Corvalta" need a business card for our Emergency Vehicle Equipment Installation and Infrastructure Security Business. We are contract designers, manufacturers and installers for Emergency Vehicle Fleets. This includes installation of Emergency Lights, Sirens, Vehicle Graphics and Radio Communications. We also supply this products to an international market. We also do consultant, and installation of high level security access, alarm and surveillance equipment for medium to large size businesses.

The design should represent a level of trust in our professionalism and expertise. It should visually display our ongoing relationship with the emergency services, but not overtake our commitment to high level security options.

Target Market(s)

Emergency Services and Businesses requiring high level security

Industry/Entity Type

Business

Contact Information for Business Card

*note complete details will be given to the winning designer for revising. The name "Mark Pelling will be used to fill in name".

Mark Pelling
Managing Director
Corvalta NZ Limited
Phone: +64 027 846 20193
Email: mark.pelling@corvalta-example.co.nz

Requirements
Must have
• Card must be in black. Using our logo on the top as supplied. Designers should try having the reverse side as a blurred image of police lights (red and blue) with our logo in greyscale in the centre (this is not particularly a requirement, but feel free to play around with this option).
Nice to have
• A card design that looks good when spot UV printed. A clean compact and graphic design. A grey scale feel on the front (excluding logo, but you can play around with that idea). Rounded smooth text.
Should not have
• Will update this section as designs come through - feel free to submit what you feel would look good.

```html
<!DOCTYPE html>
<html lang="en">
<head>
<meta charset="utf-8">
<title>Corvalta — Business Card</title>
<link rel="stylesheet" href="https://fonts.googleapis.com/css2?family=Jost:wght@400;500&display=swap">
<style>
  :root {
    --page-bg: #d9d6d2;
    --card-black: #0b0b0c;
    --card-charcoal: #2a2a2c;
    --accent-red: #d4232b;
    --deep-red: #7a0d12;
    --text-light: #e4e4e4;
    --text-soft: #cfcfcf;
  }
  * { box-sizing: border-box; margin: 0; padding: 0; }
  html, body {
    width: 1200px;
    height: 969px;
    overflow: hidden;
    background: var(--page-bg);
    font-family: "Jost", "Futura", sans-serif;
  }
  .card {
    position: absolute;
    left: 100px;
    top: 200px;
    width: 1000px;
    height: 568px;
    background: radial-gradient(ellipse at 45% 35%, var(--card-charcoal) 0%, var(--card-black) 65%);
    overflow: hidden;
  }
  .contact {
    position: absolute;
    left: 60px;
    top: 62px;
    color: var(--text-light);
  }
  .contact__name {
    font-size: 34px;
    font-weight: 500;
    color: var(--accent-red);
    letter-spacing: 0.5px;
    text-transform: uppercase;
    line-height: 1.1;
  }
  .contact__role {
    font-size: 26px;
    font-weight: 400;
    color: var(--text-soft);
    margin-top: 6px;
  }
  .contact__list {
    list-style: none;
    margin-top: 30px;
  }
  .contact__item {
    display: flex;
    align-items: center;
    gap: 14px;
    font-size: 26px;
    color: var(--text-soft);
    line-height: 1.2;
  }
  .contact__item + .contact__item { margin-top: 10px; }
  .contact__item--company { margin-bottom: 20px; }
  .contact__icon {
    width: 22px;
    height: 22px;
    flex: none;
    fill: var(--accent-red);
  }
  .brand-name {
    position: absolute;
    left: 60px;
    top: 395px;
    font-size: 70px;
    font-weight: 500;
    letter-spacing: 2px;
    color: var(--text-light);
    text-transform: uppercase;
  }
  .brand-symbol-area {
    position: absolute;
    right: 0;
    top: 0;
    width: 500px;
    height: 568px;
    background: linear-gradient(100deg, rgba(122, 13, 18, 0) 0%, var(--deep-red) 45%, var(--accent-red) 75%, #b8b8b8 100%);
  }
</style>
</head>
<body>
  <main class="card">
    <div class="brand-symbol-area" role="img" aria-label="Large brand symbol decoration in red, black and silver"></div>

    <section class="contact">
      <h1 class="contact__name">Mark Pelling</h1>
      <p class="contact__role">Managing Director</p>
      <ul class="contact__list">
        <li class="contact__item contact__item--company">
          <svg class="contact__icon" viewBox="0 0 24 24" aria-hidden="true">
            <path d="M12 1.5a7.5 7.5 0 0 0-7.5 7.5c0 5.6 7.5 13.5 7.5 13.5s7.5-7.9 7.5-13.5A7.5 7.5 0 0 0 12 1.5zm0 10.5a3 3 0 1 1 0-6 3 3 0 0 1 0 6z"/>
          </svg>
          Corvalta NZ Limited
        </li>
        <li class="contact__item">
          <svg class="contact__icon" viewBox="0 0 24 24" aria-hidden="true">
            <path d="M6.6 10.8a15.1 15.1 0 0 0 6.6 6.6l2.2-2.2a1 1 0 0 1 1-.25 11.4 11.4 0 0 0 3.6.57 1 1 0 0 1 1 1V20a1 1 0 0 1-1 1A17 17 0 0 1 3 4a1 1 0 0 1 1-1h3.5a1 1 0 0 1 1 1c0 1.25.2 2.45.57 3.57a1 1 0 0 1-.25 1z"/>
          </svg>
          +64 027 846 20193
        </li>
        <li class="contact__item">
          <svg class="contact__icon" viewBox="0 0 24 24" aria-hidden="true">
            <path d="M2 5h20v14H2z M2 5l10 7 10-7" fill="var(--accent-red)"/>
            <path d="M3 6l9 6.3L21 6" fill="none" stroke="#0b0b0c" stroke-width="1.6"/>
          </svg>
          mark.pelling@corvalta-example.co.nz
        </li>
      </ul>
    </section>

    <p class="brand-name">Corvalta</p>
  </main>
</body>
</html>
```